PowerPoint Presentation

We are looking for a new PPT layout template existing of a cover page, three internal pages - one with text bullets, one with a picture/information and one with more of a table for pricing information and the last a last "thank you - contact info" page. Feel free to grab any graphics from our website at www.brightharbor.com

Any product can be chosen from our products page. Colors are cyan and orange and feel free to choose darker backgrounds for the front and end page. Also included in the graphics is our new business card design.

Also note we are updating our website, and have attached a sample of how it looks for reference.

Reason: We are still looking for submissions for our PowerPoint presentation. We have increased the award amount as well.

Target Market(s)

Target market is private industry professionals, public safety organizations, and state and local government agencies.

Industry/Entity Type

Business

Colors
33a6d7
86cae6
cee9f5
f68d4d
f8ba93
fce2d4

```html
<!DOCTYPE html>
<html lang="en">
<head>
<meta charset="utf-8">
<title>Thank You</title>
<link rel="stylesheet" href="https://fonts.googleapis.com/css2?family=Raleway:wght@100;200&family=Gochi+Hand&family=Open+Sans:wght@300;400;700&display=swap">
<style>
  :root {
    --cyan-deep: #0a8fcc;
    --cyan: #1aa4e0;
    --cyan-light: #4cbcec;
    --navy: #003461;
    --orange: #f26a21;
    --orange-light: #fbb03b;
    --white: #ffffff;
  }
  html, body {
    margin: 0;
    padding: 0;
    overflow: hidden;
    background: var(--navy);
  }
  .slide {
    position: relative;
    width: 1200px;
    height: 900px;
    overflow: hidden;
    background: var(--navy);
  }
  .tunnel-scene {
    position: absolute;
    left: 0;
    top: 0;
    width: 1200px;
    height: 820px;
    background: radial-gradient(ellipse 620px 460px at 1110px 320px, var(--cyan-light) 0%, var(--cyan) 45%, var(--cyan-deep) 100%);
  }
  .footer-band {
    position: absolute;
    left: 0;
    top: 820px;
    width: 1200px;
    height: 80px;
    background: var(--navy);
  }
  .smile-badge {
    position: absolute;
    left: 562px;
    top: 303px;
    width: 134px;
    height: 134px;
    border-radius: 50%;
    background: radial-gradient(circle at 45% 35%, var(--orange-light) 0%, #f7941d 60%, #e57b12 100%);
  }
  .thanks-title {
    position: absolute;
    left: 380px;
    top: 444px;
    width: 450px;
    margin: 0;
    font-family: "Raleway", sans-serif;
    font-weight: 100;
    font-size: 79px;
    line-height: 1;
    letter-spacing: 1px;
    color: var(--white);
    white-space: nowrap;
  }
  .thanks-subtitle {
    position: absolute;
    left: 592px;
    top: 520px;
    margin: 0;
    font-family: "Gochi Hand", cursive;
    font-size: 29px;
    line-height: 1;
    letter-spacing: 1px;
    color: var(--white);
    white-space: nowrap;
  }
  .good-day-tag {
    position: absolute;
    left: 1032px;
    top: 801px;
    width: 96px;
    height: 99px;
    background: var(--orange);
    display: flex;
    flex-direction: column;
    align-items: center;
    justify-content: center;
    font-family: "Open Sans", sans-serif;
    font-weight: 300;
    font-size: 18px;
    line-height: 19px;
    color: var(--white);
    text-align: center;
  }
  .good-day-tag strong {
    font-weight: 700;
  }
</style>
</head>
<body>
  <main class="slide">
    <div class="tunnel-scene" role="img" aria-label="Blue arched tunnel receding into the distance with a row of business people silhouettes standing on the right"></div>
    <div class="footer-band"></div>
    <div class="smile-badge" role="img" aria-label="Orange smiley emoticon"></div>
    <h1 class="thanks-title">THANK YOU</h1>
    <p class="thanks-subtitle">FOR YOUR TIME ..!</p>
    <div class="good-day-tag">
      <span>HAVE</span>
      <span>A</span>
      <strong>GOOD</strong>
      <span>DAY</span>
    </div>
  </main>
</body>
</html>
```